Geschäftspapiere für Verkauf und Reparatur von Nähmaschinen, Stickmaschinen, etc.
Zielgruppe
Verkauf und Reparatur von Nähmaschinen, Stickmaschinen, etc.
Zielgruppe sind meist Frauen welche das Nähen beruflich ausüben oder es als Hobby betreiben
Aufgabenstellung
Wir wünschen uns eine neue Briefvorlage, welche sich mit unserem Online-Shop widerspiegelt. Alle voran soll das Layout modern sein und unser Logo in den Vordergrund bringen. Elemente aus dem Online-Shop welche unseren Familienbetrieb zeigt dürfen auf gerne enthalten sein.

```html
<!DOCTYPE html>
<html lang="de">
<head>
<meta charset="utf-8">
<title>Nadelwerk Studio – Briefvorlage</title>
<link rel="stylesheet" href="https://fonts.googleapis.com/css2?family=Work+Sans:wght@400;500;600;700;800&display=swap">
<style>
  :root {
    --brand-red: #a8322a;
    --deep-red: #7e1f1a;
    --ink: #1c1c22;
    --navy: #1f2340;
    --paper: #ffffff;
    --backdrop: #e9e6e1;
  }
  * { box-sizing: border-box; margin: 0; padding: 0; }
  html, body { width: 1200px; height: 800px; overflow: hidden; }
  body {
    background: var(--backdrop);
    font-family: "Work Sans", Arial, sans-serif;
    color: var(--ink);
    position: relative;
  }
  .letter {
    position: absolute;
    left: 320px; top: 12px;
    width: 560px; height: 776px;
    background: var(--paper);
    overflow: hidden;
    box-shadow: 0 4px 18px rgba(0,0,0,.12);
  }
  .header-swoosh { position: absolute; top: 0; right: 0; width: 560px; height: 150px; }
  .brand { position: absolute; left: 44px; top: 112px; display: flex; align-items: center; gap: 10px; }
  .brand-name {
    font-weight: 800; font-size: 26px; line-height: 0.95;
    letter-spacing: 0.5px; color: var(--ink); text-transform: uppercase;
  }
  .brand-mark { width: 22px; height: 22px; background: var(--brand-red); }
  .brand-rule { position: absolute; left: 0; top: 186px; width: 300px; height: 12px; background: var(--brand-red); }
  .recipient { position: absolute; left: 44px; top: 214px; font-size: 11px; line-height: 1.45; }
  .recipient-name { font-weight: 700; font-size: 13px; color: var(--navy); }
  .letter-date { position: absolute; right: 44px; top: 240px; font-size: 10.5px; font-weight: 700; }
  .letter-body { position: absolute; left: 44px; right: 44px; top: 292px; font-size: 11px; line-height: 1.55; font-weight: 500; }
  .letter-body p { margin-bottom: 20px; text-align: justify; }
  .closing { position: absolute; left: 44px; top: 520px; font-size: 11px; font-weight: 700; }
  .signature { position: absolute; left: 44px; top: 546px; width: 120px; height: 36px; background: #efefef; }
  .signer { position: absolute; left: 44px; top: 592px; font-size: 11px; line-height: 1.35; }
  .signer-name { font-weight: 700; }
  .footer-rule { position: absolute; left: 44px; right: 44px; height: 2px; background: var(--ink); }
  .footer-rule.top { top: 640px; }
  .footer-rule.bottom { top: 736px; background: var(--navy); }
  .newsletter { position: absolute; left: 44px; right: 44px; top: 650px; font-size: 10px; font-weight: 500; }
  .contact-row { position: absolute; left: 44px; right: 44px; top: 682px; display: flex; justify-content: space-between; align-items: center; }
  .contact-item { display: flex; align-items: center; gap: 7px; font-size: 10.5px; font-weight: 700; }
  .contact-icon { width: 26px; height: 26px; }
</style>
</head>
<body>
  <main class="letter">
    <svg class="header-swoosh" viewBox="0 0 560 150" aria-hidden="true">
      <path d="M300 0 H560 V150 C520 90 470 50 380 38 C340 32 310 20 300 0 Z" fill="var(--deep-red)"/>
      <path d="M250 0 H560 V110 C510 60 450 40 370 36 C320 34 280 20 250 0 Z" fill="var(--brand-red)"/>
      <path d="M200 60 C280 40 360 40 430 58 C370 50 290 52 200 66 Z" fill="var(--ink)"/>
    </svg>

    <div class="brand">
      <div class="brand-name">Nadelwerk<br>Studio</div>
      <div class="brand-mark"></div>
    </div>
    <div class="brand-rule"></div>

    <address class="recipient" style="font-style:normal">
      <div class="recipient-name">Lena Hofbauer</div>
      <div>hallo@beispielpost.de</div>
      <div>Lindenweg 8, 79098 Musterstadt</div>
    </address>

    <div class="letter-date">15 January, 2023</div>

    <section class="letter-body">
      <p>Lorem ipsum dolor sit amet, consectetur adipiscing elit. Fusce placerat purus ac ipsum sodales ornare. Proin libero arcu, vehicula eu orci sed, venenatis facilisis lacus. Vivamus tincidunt auctor felis, a faucibus massa rhoncus eu. Fusce at vehicula ligula, a posuere nisl. Nullam maximus fermentum fringilla. Nullam convallis, felis quis ullamcorper dictum, purus lorem luctus augue, et iaculis justo tellus vitae ligula. Suspendisse varius erat vel dolor convallis, ac aliquet metus feugiat.</p>
      <p>Lorem ipsum dolor sit amet, consectetur adipiscing elit. Fusce placerat purus ac ipsum sodales ornare. Proin libero arcu, vehicula eu orci sed, venenatis facilisis lacus. Vivamus tincidunt auctor felis, a faucibus massa rhoncus eu. Fusce at vehicula ligula, a posuere nisl. Nullam maximus fermentum fringilla. Nullam convallis, felis quis ullamcorper dictum, purus lorem luctus augue, et iaculis justo tellus vitae ligula. Suspendisse varius erat vel dolor convallis, ac aliquet metus feugiat.</p>
    </section>

    <div class="closing">Warm Regards,</div>
    <div class="signature" role="img" aria-label="Handschriftliche Unterschrift"></div>
    <div class="signer">
      <div class="signer-name">Marta Keller</div>
      <div>General Manager</div>
    </div>

    <div class="footer-rule top"></div>
    <div class="newsletter">info@nadelwerk-studio.de Newsletter-Anmeldung</div>
    <div class="contact-row">
      <div class="contact-item">
        <svg class="contact-icon" viewBox="0 0 26 26" aria-hidden="true">
          <circle cx="13" cy="13" r="13" fill="var(--brand-red)"/>
          <path d="M9 7 L11.5 7 L12.5 10 L11 11.3 C11.8 13 13 14.2 14.7 15 L16 13.5 L19 14.5 L19 17 C19 18 18 19 17 19 C12 18.5 7.5 14 7 9 C7 8 8 7 9 7 Z" fill="#fff"/>
        </svg>
        <span>49 (0)7421/58 30</span>
      </div>
      <div class="contact-item">
        <svg class="contact-icon" viewBox="0 0 26 26" aria-hidden="true">
          <circle cx="13" cy="13" r="13" fill="var(--brand-red)"/>
          <rect x="7" y="8.5" width="12" height="9" fill="none" stroke="#fff" stroke-width="1.4"/>
          <path d="M7 8.5 L13 13.5 L19 8.5" fill="none" stroke="#fff" stroke-width="1.4"/>
        </svg>
        <span>info@nadelwerk-studio.de</span>
      </div>
      <div class="contact-item">
        <svg class="contact-icon" viewBox="0 0 26 26" aria-hidden="true">
          <circle cx="13" cy="13" r="13" fill="var(--brand-red)"/>
          <circle cx="13" cy="13" r="6.5" fill="none" stroke="#fff" stroke-width="1.3"/>
          <ellipse cx="13" cy="13" rx="3" ry="6.5" fill="none" stroke="#fff" stroke-width="1.1"/>
          <path d="M6.5 13 H19.5 M7.5 10 H18.5 M7.5 16 H18.5" stroke="#fff" stroke-width="1"/>
        </svg>
        <span>www.nadelwerk-studio.de</span>
      </div>
    </div>
    <div class="footer-rule bottom"></div>
  </main>
</body>
</html>
```